Healthcare IT company looking for business card design

We develop IT systems for healthcare that significantly reduces cost and improves quality.

We want a business card design that is professional and clean, and using the colors in our logo.

Target Market(s)

Doctors and decision makers in the healthcare industry

Industry/Entity Type

Healthcare

Contact Information for Business Card

It should include
Name and title, address, telephone

Tobias Vrenholt, CEO
+46 712 418257
tobias@kelvaro.se

Font styles to use
Serif

Colors
0355a3
ed282f

Requirements
Must have
• Clean design
• Professional feel
Nice to have
• N/A
Should not have
• N/A

```html
<!DOCTYPE html>
<html lang="en">
<head>
<meta charset="utf-8">
<title>Kelvaro — Business Card</title>
<link rel="stylesheet" href="https://fonts.googleapis.com/css2?family=Open+Sans:wght@400;600;700&display=swap">
<style>
  :root {
    --brand-blue: #0355a3;
    --card-white: #ffffff;
    --stage: #e9ebee;
    --text-light: #ffffff;
    --shadow: rgba(20, 30, 45, 0.18);
  }
  * { margin: 0; padding: 0; box-sizing: border-box; }
  html, body {
    width: 1200px;
    height: 864px;
    overflow: hidden;
    background: var(--stage);
    font-family: "Open Sans", Arial, sans-serif;
  }
  .sheet {
    width: 1200px;
    height: 864px;
    display: flex;
    flex-direction: column;
    align-items: center;
    justify-content: center;
    gap: 48px;
  }
  .card {
    width: 560px;
    height: 320px;
    border-radius: 4px;
    box-shadow: 0 10px 28px var(--shadow);
    position: relative;
    overflow: hidden;
  }
  .card-front {
    background: var(--card-white);
    display: flex;
    align-items: center;
    justify-content: center;
  }
  .company-name {
    color: var(--brand-blue);
    font-weight: 600;
    font-size: 60px;
    line-height: 1;
  }
  .card-back {
    background: var(--brand-blue);
    color: var(--text-light);
    text-align: center;
    padding-top: 50px;
  }
  .holder-name {
    font-weight: 700;
    font-size: 19px;
    letter-spacing: 0.5px;
    text-transform: uppercase;
  }
  .holder-title {
    font-size: 14px;
    margin-top: 1px;
  }
  .divider {
    width: 210px;
    margin: 14px auto 20px;
    border-top: 1.5px dashed var(--text-light);
  }
  .address {
    font-size: 15px;
    line-height: 1.5;
  }
  .contact {
    margin-top: 20px;
    font-size: 15px;
    line-height: 1.5;
  }
  .contact-label { font-weight: 700; }
</style>
</head>
<body>
  <main class="sheet">
    <section class="card card-front" aria-label="Card front">
      <span class="company-name">Kelvaro</span>
    </section>

    <section class="card card-back" aria-label="Card back">
      <h1 class="holder-name">Tobias Vrenholt</h1>
      <p class="holder-title">CEO</p>
      <div class="divider" aria-hidden="true"></div>
      <p class="address">12345, Address Goes Here<br>Country Name, 123456</p>
      <p class="contact">
        <span class="contact-label">Phone:</span> +46 712 418257<br>
        <span class="contact-label">Email:</span> tobias@kelvaro.se
      </p>
    </section>
  </main>
</body>
</html>
```